ECサイトのブランドコンセプトページ、商品ページ、プロモーションページのデザインをおねがいします。HTMLコーディングは含みません。

基本的な掲載コンテンツに変更はありません。添付のワイヤーを基に、フラワーショップのスイーツ店らしいシンプルで上品なデザインを希望します。作成頂いたコンセプトページをベースに他のページも制作したいと考えているため、その点も考慮して下さい。ロゴは添付ファイルのものを利用ください。

・デバイスフォントはWin "小塚ゴシック"、Mac "ヒラギノゴシック"、色がアースカラー。
・ターゲットは、30代~50代。スイーツ、花などの贈り物の購入者や、女子会、ホームパーティーでの購入者を想定。
・配色、クリエイティブは、参考サイトを参照。
[参考サイト]
http://www.morvanette.jp/
http://www.tolvicane.co.jp/

サイトリリース時にデザインに手を加えることをご了承ください。

ご質問・ご確認事項ありましたら「この依頼に質問」からお願いします。
それではたくさんのご応募お待ちしております。
3ページ
アースカラー、ピンク、ホワイト、
選定後納品ファイルですが、レイヤー情報を保持した.ai,.psdのいずれかを納品いただきます。当方、Win版CS5。
情報が少なかったので追記致します。

商品ページは全ての商品に共通したデザイン・キャッチコピーをおねがいします。
商品ページのイメージは下記サイトを参考にお願いします。

http://www.zenkuro8.com/menu/premiumcheesetart/

プロモーションページは下記サイトのような特集を組んで商品ページに誘導するイメージです

http://www.dorimenasu.com/new.php?twn=327
たくさんのご提案ありがとうございました。

ただ今、選考中です。
今しばらくお待ちください。
選定にお時間をいただき申し訳ございません。
とても良い提案が多く、クライアントの方でも決めかねております。

現在、クライアントの方で当選候補者様を数名に絞っていただいてるのですが、クライアントから候補者様のデザインされたプロモーションページが見たいという要望がございまして、ご応募いただいたランサー様に大至急、プロモーションページのデザインをお願い致します。当選候補者様には個別で修正依頼として、お願いを致します。修正依頼のないランサー様には申し訳ございませんが、ご了承ください。

プロモーションページをご提案いただけた方の中から必ず当選者を選ばせて頂くことを確約致します。
ご対応いただいている皆様
要件急変、大変申し訳ございません。

クライアントの方でこんなイメージも見たい、あんなイメージも見たいと意見が二転三転しておりまして、あれもこれもと対応していただくわけにはいかないので、ナビの画像など無しで小さめのおしゃれなフォントにしていただくだけで構いません。
プロモーションのページについては下記参考サイトのような白背景にフォントと余白で魅せるデザインでお願いできないでしょうか?

レイアウトはワイヤーの通りで構いません。

参考:http://vetrune-online.com/

お手数おかけして申し訳ございませんが、何卒よろしくお願い致します。

急な変更にご対応いただいているランサー様。
ありがとうございます。

ご提案いただいた案は全て、クライアントに提示致します。
ご提案いただいた案の中から必ず当選者を確定することを約束致します。

当選者のランサー様には当選したデザイン案でのブランドコンセプトページ、
商品ページの修正をお願い致します。お手数ではございますが、何卒ご了承くださいますようよろしくお願い申し上げます。
急な変更にも関わらず、ご対応いただきましたランサーの皆様、ありがとうございます。

現在、ご提案いただいたプロモーションページのデザインをクライアントに提出し選定中でございます。

提出致しましたデザインの中から当選者様を選ばせて頂きます。

当選者様には、お手数ではございますが、当選デザインでの商品ページ、コンセプトページの修正をお願い致しますこと、ご了承くださいますようお願い申し上げます。
当選者様は決定しているのですが、まだ修整をお願いすることがございまして、当選の確定を控えさせていただいております。

ご提案を頂いたランサーの皆様がたには、当選の確定をお待たせしてしまっていることお詫び申し上げます。

シンプルな中にも品があり、クライアント様の受けもよく、度重なる修正のお願いにもご対応いただき、クライアント様のイメージに近づけることができました。ありがとうございます。

急な要件変更にも関わらず、ご対応いただきましたランサーの皆様、ありがとうございました。

```html
<!DOCTYPE html>
<html lang="ja">
<head>
<meta charset="utf-8">
<title>Roll Cake | Fleurelle</title>
<link href="https://fonts.googleapis.com/css2?family=Cormorant+Garamond:wght@400;600&family=Noto+Sans+JP:wght@400;700&display=swap" rel="stylesheet">
<style>
:root{
  --pink:#e9cfd0;
  --brown:#5b4a40;
  --brown-soft:#8a786c;
  --gold:#c9a25e;
  --rose:#c8737b;
  --bg:#f3f1ef;
  --white:#ffffff;
  --line:#d8d2cc;
  --button:#f4b843;
  --button-edge:#d99d2a;
  --photo-a:#e7c6c3;
  --photo-mid:#f6ece6;
  --photo-b:#b98a7e;
  --panel:#8c8c8c;
  --link:#4a6fb5;
}
*{box-sizing:border-box;margin:0;padding:0}
html,body{width:1200px;height:3456px;overflow:hidden}
body{background:var(--bg);color:var(--brown);font-family:"Noto Sans JP",sans-serif;font-size:15px;line-height:1.7;position:relative}
.header{position:absolute;left:0;top:0;width:1200px;height:170px;background:var(--pink)}
.header__lead{position:absolute;left:16px;top:10px;font-size:12px;color:var(--brown-soft)}
.brand{position:absolute;left:0;top:50px;width:1200px;display:flex;justify-content:center;align-items:center;gap:12px}
.brand__mark{width:14px;height:14px;background:var(--brown)}
.brand__name{font-family:"Noto Sans JP",sans-serif;font-size:30px;font-weight:400;color:var(--brown);letter-spacing:4px;line-height:1}
.header__links{position:absolute;right:20px;top:10px;font-size:12px;color:var(--brown)}
.cart-link{position:absolute;right:20px;top:46px;background:var(--white);border:1px solid var(--line);font-size:12px;padding:4px 12px}
.nav{position:absolute;left:0;top:170px;width:1200px;height:56px;background:var(--white);border-bottom:1px solid var(--line);display:flex;justify-content:center}
.nav a{font-family:"Cormorant Garamond",serif;font-size:26px;color:var(--brown);text-decoration:none;padding:8px 26px;border-right:1px solid var(--line)}
.nav a:last-child{border-right:none}
.crumb{position:absolute;left:16px;top:232px;font-size:13px;color:var(--brown-soft)}
.crumb a{color:var(--link)}
.side{position:absolute;left:16px;top:272px;width:240px}
.side h2{font-family:"Cormorant Garamond",serif;font-size:32px;font-weight:600;border-bottom:1px solid var(--line);padding-bottom:4px;margin-bottom:14px}
.side li{list-style:none;border-bottom:1px dotted var(--line);padding:10px 0;font-family:"Cormorant Garamond",serif;font-size:18px;line-height:1.3}
.side li span{display:block;font-family:"Noto Sans JP",sans-serif;font-size:13px;color:var(--brown-soft)}
.banner{position:absolute;left:16px;width:240px;background:var(--panel)}
.main{position:absolute;left:304px;top:262px;width:856px}
.title{font-family:"Cormorant Garamond",serif;font-size:52px;font-weight:600;line-height:1}
.title small{font-family:"Noto Sans JP",sans-serif;font-size:18px;font-weight:400}
.photo{background:linear-gradient(135deg,var(--photo-a),var(--photo-mid) 45%,var(--photo-b))}
.hero{width:856px;height:390px;margin-top:18px}
.caption{text-align:right;font-size:12px;color:var(--brown-soft);margin-top:6px}
.lead-title{font-size:28px;font-weight:700;margin-top:8px;line-height:1.4}
.text{font-size:16px;line-height:1.75}
.button{display:inline-block;background:var(--button);color:var(--brown);border-radius:8px;padding:8px 22px;font-size:15px;font-weight:700;border:1px solid var(--button-edge)}
.block-title{position:absolute;left:0;width:856px}
.section-title{font-size:32px;font-weight:700;border-bottom:2px solid var(--line);padding-bottom:6px;line-height:1.4}
.point{position:absolute;left:0;width:856px;height:220px}
.point h3{font-family:"Cormorant Garamond",serif;font-size:34px;color:var(--gold);border-bottom:1px solid var(--gold);width:420px;font-weight:600;line-height:1.3}
.point .text{width:420px;margin-top:14px}
.point .photo{position:absolute;right:0;top:10px;width:420px;height:200px}
.review{position:absolute;left:0;width:856px}
.review h4{font-size:15px;color:var(--rose);border-bottom:1px dotted var(--line);padding-bottom:4px;display:flex;justify-content:space-between}
.review h4 span{color:var(--brown-soft);font-weight:400}
.review p{font-size:16px;margin-top:10px}
.buy-main{position:absolute;left:0;top:2364px;width:420px;height:260px}
.thumbs{position:absolute;left:0;top:2636px;display:flex;gap:8px}
.thumbs div{width:98px;height:64px}
.buy-table{position:absolute;left:436px;top:2364px;width:420px;height:330px;background:var(--white);border:1px solid var(--line);padding:14px 20px}
.buy-table dl{display:grid;grid-template-columns:120px 1fr;row-gap:14px;font-size:16px}
.buy-table dd{border-bottom:1px solid var(--line)}
.info{position:absolute;background:var(--white);border:1px solid var(--line);padding:10px;font-size:12px;line-height:1.6}
.info h5{font-size:13px;border-bottom:1px solid var(--line);margin-bottom:8px;display:flex;justify-content:space-between}
.info h5 em{font-style:normal;background:var(--line);padding:0 6px;font-size:11px}
.free{font-size:38px;font-weight:700;color:var(--brown);text-align:center;line-height:1.4}
.cards{display:flex;gap:6px;margin-top:8px}
.cards span{width:46px;height:28px;background:var(--line);border-radius:3px}
.footer{position:absolute;left:0;top:3330px;width:1200px;height:126px;background:var(--pink)}
</style>
</head>
<body>
<header class="header">
  <p class="header__lead">店舗案内文店舗案内文店舗案内文店舗案内文</p>
  <div class="brand"><span class="brand__mark"></span><span class="brand__name">Fleurelle</span></div>
  <p class="header__links">ご利用ガイド ｜ 会員登録 ｜ ログイン ｜ お問い合わせ</p>
  <p class="cart-link">カートを見る</p>
</header>
<nav class="nav"><a>HOME</a><a>Concept</a><a>Product</a><a>Promotion</a><a>Monitor</a><a>Column</a><a>Login</a></nav>
<p class="crumb"><a>Top</a> &gt; <a>Sweets</a> &gt; Roll Cake</p>

<aside class="side">
  <h2>Sweets</h2>
  <ul>
    <li>Roll cake<span>-ロールケーキ-</span></li>
    <li>Cheese tart<span>-チーズタルト-</span></li>
    <li>Rosewater macaron<span>-ローズウォーターマカロン-</span></li>
    <li>Baked sweets<span>-焼き菓子-</span></li>
    <li>Boule de neige<span>-ブールドネージュ-</span></li>
    <li>Meringue<span>-メレンゲ-</span></li>
  </ul>
</aside>
<div class="banner" style="top:932px;height:390px" role="img" aria-label="バナー枠"></div>
<div class="banner" style="top:1448px;height:384px" role="img" aria-label="バナー枠"></div>

<main class="main">
  <h1 class="title">Roll Cake <small>-ロールケーキ-</small></h1>
  <div class="hero photo" role="img" aria-label="ローズ色のロールケーキと紅茶の写真"></div>
  <p class="caption">直径6cm×長さ24cm 奥の紅茶はローズティー、ローズウォーター使用</p>
  <h2 class="lead-title">バラ香るロールケーキ</h2>
  <p class="text">ロールの香りを古都の花弁でさりげなく香る<br>朝摘みした古都を、水蒸気蒸留により抽出した特製のローズ水を使用しています。<br>優雅な香りで、爽やかな香りをお楽しみください。</p>
  <p style="margin-top:8px"><span class="button">🛒 カートに入れる</span></p>

  <div class="block-title" style="top:740px"><h2 class="section-title">こだわりポイント</h2></div>
  <section class="point" style="top:900px"><h3>Point1</h3><p class="text">ロールの香りを古都の花弁でさりげなく香る朝摘みした古都を、水蒸気蒸留により抽出した特製のローズ水を使用しています。</p><div class="photo" role="img" aria-label="ロールケーキの断面写真"></div></section>
  <section class="point" style="top:1172px"><h3>Point2</h3><p class="text">ロールの香りを古都の花弁でさりげなく香る朝摘みした古都を、水蒸気蒸留により抽出した特製のローズ水を使用しています。</p><div class="photo" role="img" aria-label="紅茶とロールケーキの写真"></div></section>
  <section class="point" style="top:1460px"><h3>Point3</h3><p class="text">ロールの香りを古都の花弁でさりげなく香る朝摘みした古都を、水蒸気蒸留により抽出した特製のローズ水を使用しています。</p><div class="photo" role="img" aria-label="ロールケーキ全体の写真"></div></section>
  <p style="position:absolute;left:0;top:1700px"><span class="button">🛒 カートに入れる</span></p>

  <div class="block-title" style="top:1810px"><h2 class="section-title">テスト商品モニターの声</h2></div>
  <section class="review" style="top:1900px"><h4>薔薇の香りがふわりと広がる<span>世田谷区　Aさん(31) 女性</span></h4><p>ここに感想が入ります。メイリオ14px。ここに感想が入ります。メイリオ14px。ここに感想が入ります。メイリオ14px。ここに感想が入ります。メイリオ14px。</p></section>
  <section class="review" style="top:2040px"><h4>華やかな食感でした<span>世田谷区　Aさん(31) 女性</span></h4><p>ここに感想が入ります。メイリオ14px。ここに感想が入ります。メイリオ14px。ここに感想が入ります。メイリオ14px。</p></section>

  <div class="block-title" style="top:2280px"><h2 class="section-title">ご購入</h2></div>
  <div class="buy-main photo" role="img" aria-label="ロールケーキと紅茶の商品写真"></div>
  <div class="thumbs"><div class="photo" role="img" aria-label="商品写真1"></div><div class="photo" role="img" aria-label="商品写真2"></div><div class="photo" role="img" aria-label="商品写真3"></div><div class="photo" role="img" aria-label="商品写真4"></div></div>
  <div class="buy-table">
    <dl><dt>商品名</dt><dd>&nbsp;</dd><dt>価格</dt><dd>&nbsp;</dd><dt>オプション</dt><dd>&nbsp;</dd><dt>数量</dt><dd>&nbsp;</dd></dl>
    <p style="text-align:right;margin-top:36px"><span class="button">🛒 カートに入れる</span></p>
  </div>

  <div class="info" style="left:0;top:2710px;width:272px;height:150px"><h5>配送・送料について<em>詳細</em></h5><p class="free">送料無料！</p><p>全国一律で配送いたします。</p></div>
  <div class="info" style="left:0;top:2870px;width:272px;height:150px"><h5>お支払いについて<em>詳細</em></h5><p>お支払い方法はクレジットカード、代金引換、銀行振込からお選びいただけます。</p><div class="cards"><span></span><span></span><span></span><span></span></div></div>
  <div class="info" style="left:292px;top:2710px;width:272px;height:150px"><h5>商品のお届けについて<em>詳細</em></h5><p>ご注文確認後、三営業日以内に発送いたします。お届け日のご指定も承ります。</p></div>
  <div class="info" style="left:292px;top:2870px;width:272px;height:150px"><h5>返品・交換について<em>詳細</em></h5><p>生菓子のためお客様都合による返品はお受けできません。不良品は交換いたします。</p></div>
  <div class="info" style="left:584px;top:2710px;width:272px;height:310px"><h5>営業日・店舗案内<em>詳細</em></h5><p style="color:var(--rose)">【営業時間】<br>平日 10:00〜18:00</p><p>土日祝日はメール受付のみ。お問い合わせは翌営業日に順次ご返信いたします。店舗では季節の花とスイーツをご用意しております。</p></div>
</main>
<footer class="footer"></footer>
</body>
</html>
```